Business Card Design

Consultation for design, construction athletic facilities specializing in synthetic turf systems and all weather running track systems.
Motto "True Owner Representation"
New Company that we'd like to highlight the LOGO first and foremost with the colors of the background and font as primary colors of the card too if possible. I've also attached a typical larger project design layout that could be used in the background to highlight our design and construction specialty.
Website is something we want very noticeable for driving traffic.
Target Market(s)
Athletic Directors, Designers, Government and Military, Contractors
Industry/Entity Type
Construction
Contact Information for Business Card
Peter L. Vandrell CFB, CTB
48317 W 63rd Ave
Harlow Ridge, WA 99482
C +1 503.555.0147
O +1 808.555.0182
Peter@fieldlaneco.example
www.fieldlaneco.example

```html
<!DOCTYPE html>
<html lang="en">
<head>
<meta charset="utf-8">
<title>Corvane Sport — Business Card</title>
<link rel="stylesheet" href="https://fonts.googleapis.com/css2?family=Arimo:wght@400;700&display=swap">
<style>
  :root {
    --backdrop: #d9d9d7;
    --card-black: #050505;
    --orange: #e2601b;
    --peach: #f3c8a8;
    --silver: #f1f1f0;
    --ink: #111111;
    --line-black: #0d0d0d;
    --watermark: rgba(120, 120, 120, 0.26);
    --paper: #fbfbfa;
    --plan-tone: #e9e9e7;
  }
  * { box-sizing: border-box; margin: 0; padding: 0; }
  html, body {
    width: 1200px; height: 1200px; overflow: hidden;
    background: var(--backdrop);
    font-family: "Arimo", Arial, sans-serif;
  }
  .canvas { position: relative; width: 1200px; height: 1200px; }

  /* ---------- back of card ---------- */
  .card-back {
    position: absolute; left: 430px; top: 150px;
    width: 660px; height: 377px;
    background: var(--card-black);
    box-shadow: 0 10px 28px rgba(0,0,0,0.35);
  }
  .rule {
    position: absolute; height: 5px;
    background: linear-gradient(90deg, var(--orange) 0%, #8a4a2a 45%, #5a3a2a 60%, var(--orange) 100%);
  }
  .card-back .rule-top { left: 150px; right: 40px; top: 40px; }
  .card-back .rule-bottom { left: 60px; right: 90px; bottom: 45px; }
  .brand {
    position: absolute; left: 150px; top: 140px;
    display: flex; align-items: center; gap: 22px;
  }
  .brand-mark {
    width: 70px; height: 70px; border-radius: 50%;
    border: 3px solid var(--orange);
  }
  .brand-name {
    color: var(--orange);
    font-weight: 400; font-size: 52px; letter-spacing: 6px;
    line-height: 1;
  }

  /* ---------- front of card ---------- */
  .card-front {
    position: absolute; left: 110px; top: 470px;
    width: 700px; height: 400px;
    background: linear-gradient(100deg, var(--peach) 0%, var(--silver) 45%, #e6e6e4 70%, var(--peach) 100%);
    box-shadow: 0 12px 30px rgba(0,0,0,0.35);
    overflow: hidden;
  }
  .name-strip {
    position: absolute; left: 0; top: 0; width: 475px; height: 45px;
    background: var(--paper);
  }
  .holder-name {
    position: absolute; left: 42px; top: 14px;
    font-weight: 700; font-size: 17px; color: var(--ink);
  }
  .credentials {
    position: absolute; left: 395px; top: 62px;
    font-weight: 700; font-size: 8px; color: var(--ink);
  }
  .bar { position: absolute; }
  .bar.orange { background: var(--orange); }
  .bar.black { background: var(--line-black); }

  .site-plan {
    position: absolute; left: 482px; top: 0;
    width: 218px; height: 200px;
    background: linear-gradient(135deg, var(--paper), var(--plan-tone));
  }
  .watermark {
    position: absolute; left: 285px; top: 222px;
    color: var(--watermark); font-weight: 400;
    font-size: 34px; letter-spacing: 6px; line-height: 1;
    white-space: nowrap;
  }
  .address {
    position: absolute; left: 42px; top: 118px;
    font-weight: 700; font-size: 15px; line-height: 19px; color: var(--ink);
  }
  .phones {
    position: absolute; left: 42px; top: 185px;
    font-weight: 700; font-size: 13px; line-height: 18px; color: var(--ink);
    list-style: none;
  }
  .phones li { display: flex; align-items: center; gap: 4px; }
  .phone-tag {
    display: inline-block; width: 14px; height: 14px;
    background: var(--orange); border: 1.5px solid var(--ink);
    font-size: 10px; line-height: 11px; text-align: center;
  }
  .contact-band {
    position: absolute; left: 0; right: 0; top: 272px; bottom: 0;
    background: var(--orange);
  }
  .email {
    position: absolute; left: 42px; top: 22px;
    font-weight: 700; font-size: 13px; color: var(--ink);
  }
  .website {
    position: absolute; right: 40px; bottom: 30px;
    font-weight: 700; font-size: 15px; color: var(--ink);
  }
</style>
</head>
<body>
<main class="canvas">

  <section class="card-back" aria-label="Card back">
    <div class="rule rule-top"></div>
    <div class="brand">
      <span class="brand-mark"></span>
      <span class="brand-name">CORVANE SPORT</span>
    </div>
    <div class="rule rule-bottom"></div>
  </section>

  <section class="card-front" aria-label="Card front">
    <div class="name-strip"></div>

    <div class="contact-band">
      <span class="email">Peter@fieldlaneco.example</span>
      <span class="website">www.fieldlaneco.example</span>
    </div>

    <div class="watermark">CORVANE SPORT</div>

    <div class="site-plan" role="img" aria-label="Athletic facility site plan drawing with running track, turf field and ball fields"></div>

    <div class="bar orange" style="left:0; top:44px; width:478px; height:4px;"></div>
    <div class="bar black"  style="left:0; top:52px; width:478px; height:4px;"></div>
    <div class="bar black"  style="left:468px; top:0; width:4px; height:215px;"></div>
    <div class="bar orange" style="left:476px; top:0; width:4px; height:200px;"></div>
    <div class="bar orange" style="left:440px; top:200px; width:260px; height:4px;"></div>
    <div class="bar black"  style="left:456px; top:208px; width:244px; height:4px;"></div>

    <h1 class="holder-name">Peter L. Vandrell</h1>
    <span class="credentials">CFB, CTB</span>

    <p class="address">48317 W 63rd Ave Harlow Ridge,<br>WA 99482.</p>
    <ul class="phones">
      <li><span class="phone-tag">C</span>+1 503.555.0147</li>
      <li><span class="phone-tag">O</span>+1 808.555.0182</li>
    </ul>
  </section>

</main>
</body>
</html>
```